Analytics/BI tech start-up seeks sharp, creative, simple, secret agent type logo & theme

"Quarry 7 Technologies" seeks a logo design/color scheme template for NYC based tech start-up of software engineers, solutions architects, and data/BI analysts. We develop reporting solutions and analytics platforms for small-medium sized businesses. We code for database, cloud, and web/mobile apps.<br/><br/>Some *very basic, limited* sketches are attached to show ideas we've had. We need a logo and color scheme that may be used for business cards, paper letterhead and envelopes, and web pages to be published at "www.quarry7.dev".<br/><br/>We like the black/red, red/white, blue/black, white/black contrasts as a stating point, and prefer black background business cards, but open to anything if it feels like a good match. We are relying on the projects submitted here to take care of the creativity part of our image, which we work on logistics to launching our start-up. Something that could also be easily translated into black/white, grayscale would be appreciated as well. while log is important, we also need an icon that may be used as an app thumbnail. For font, we prefer all caps.<br/><br/>Business: Quarry 7 Technologies<br/>Slogan: If. Else. Us. / If -> Else -> Us / If - Else - Us / etc.<br/>Website: www.quarry.dev<br/>Icon: [Q7] , only as a starting point<br/>Theme Ideas: Sleek, futuristic, secret agent-like tech, simple, bold color contrasts, software code related<br/><br/>Feel free to reach out to jvorenko@mailbarn.example as a contact for any questions or follow up. We look forward to seeing amazing ideas!
Updates

We would like to provide the opportunity for as many different submissions as possible.

Target Market(s)

Small business owners, entrepreneurs, financial/tech companies, freelance engineers, people in need of IT assistance to elevate business

Industry/Entity Type

It Company

Contact Information for Business Card

Individual Info: Name, Position, Phone Number 1, Phone Number 2 (optional), Fax Number, email Address.
Company Info: Name, logo, icon (optional), web site, slogan

Font styles to use
Sans Serif
Other font styles liked:
• Similar to Biome Light All Caps, Hollow Meridian type style

Requirements
Must have
• Pronounced 1 in the logo, either in the word Section or not. Bold color contrast, one side with only logo or icon, possible web address too. Other side with all individual info plus logo, and/or icon and web address. If using uploaded files as a base, center the C more between the E and T, it is too closer to the T as is.
Nice to have
• Bolder font possibly, more square edged at ends of letters but still with minor curved corners. Icon suggested as a starting point is “[Q7]” and instead of a slogan, use "Data - Cloud - Web - Software" and the dividers don't necessary have to be hyphens.
Should not have
• Open to all creative ideas, try anything. Please come up with different logos than are in the attached files, they are meant as a starting point.

```html
<!DOCTYPE html>
<html lang="en">
<head>
<meta charset="utf-8">
<title>Quarry 7 Technologies — Business Cards</title>
<link rel="stylesheet" href="https://fonts.googleapis.com/css2?family=Roboto:wght@400;700;900&display=swap">
<style>
  :root {
    --stage: #1b1b1b;
    --card-dark: #121212;
    --card-light: #ececec;
    --green: #36a514;
    --green-bright: #3cb416;
    --ink: #1a1a1a;
    --ink-soft: #3a3a3a;
    --rule: #b9b9b9;
    --white: #ffffff;
    --web-ink: #1d2a4a;
  }
  * { box-sizing: border-box; margin: 0; padding: 0; }
  html, body { width: 1200px; height: 900px; overflow: hidden; }
  body {
    background: var(--stage);
    font-family: "Roboto", Arial, sans-serif;
    position: relative;
  }
  .card {
    position: absolute;
    width: 580px;
    height: 330px;
    left: 310px;
    border-radius: 4px;
    box-shadow: 0 14px 34px rgba(0,0,0,.55);
  }
  /* Back side */
  .card--back { top: 100px; background: var(--card-dark); color: var(--white); }
  .back-brand {
    position: absolute; left: 0; right: 0; top: 92px;
    display: flex; align-items: center; justify-content: center; gap: 18px;
  }
  .brand-square { width: 74px; height: 74px; background: var(--green); flex: none; }
  .back-brand .brand-name {
    font-weight: 900; font-size: 30px; letter-spacing: 1px;
    text-transform: uppercase; color: var(--white); line-height: 1.05;
  }
  .tagline {
    position: absolute; left: 0; right: 0; bottom: 62px;
    display: flex; justify-content: center; align-items: center; gap: 12px;
    font-size: 16px; color: var(--white);
  }
  .tagline .dot { width: 7px; height: 7px; background: var(--green-bright); }

  /* Front side */
  .card--front { top: 470px; background: var(--card-light); color: var(--ink); }
  .front-brand {
    position: absolute; left: 40px; top: 96px; width: 236px;
  }
  .front-brand .brand-square { width: 70px; height: 70px; margin-bottom: 16px; }
  .front-brand .brand-name {
    font-weight: 900; font-size: 28px; line-height: 1.05;
    text-transform: uppercase; color: var(--ink); letter-spacing: .5px;
  }
  .divider {
    position: absolute; left: 296px; top: 50px; width: 1px; height: 180px;
    background: var(--rule);
  }
  .contact { position: absolute; left: 320px; top: 52px; }
  .person-name {
    font-weight: 700; font-size: 19px; color: var(--green); letter-spacing: .5px;
  }
  .person-role { font-size: 15px; color: var(--ink-soft); margin-bottom: 16px; }
  .contact-lines { list-style: none; font-size: 15px; line-height: 1.35; }
  .contact-lines li { display: flex; align-items: center; gap: 8px; }
  .contact-lines svg { width: 13px; height: 13px; fill: var(--green); flex: none; }
  .address { font-size: 15px; line-height: 1.35; margin-top: 16px; margin-left: 21px; }
  .web {
    position: absolute; left: 320px; bottom: 40px;
    font-size: 16px; letter-spacing: 1.5px; color: var(--web-ink);
  }
  .web .accent { color: var(--green); }
</style>
</head>
<body>
  <section class="card card--back" aria-label="Card back">
    <div class="back-brand">
      <span class="brand-square"></span>
      <span class="brand-name">Quarry 7<br>Technologies</span>
    </div>
    <p class="tagline">
      <span>Data</span><span class="dot"></span>
      <span>Cloud</span><span class="dot"></span>
      <span>Web</span><span class="dot"></span>
      <span>Development</span>
    </p>
  </section>

  <section class="card card--front" aria-label="Card front">
    <div class="front-brand">
      <div class="brand-square"></div>
      <p class="brand-name">Quarry 7<br>Technologies</p>
    </div>
    <div class="divider"></div>
    <div class="contact">
      <p class="person-name">LORUM SMITH</p>
      <p class="person-role">Managing Director</p>
      <ul class="contact-lines">
        <li><svg viewBox="0 0 16 16" aria-hidden="true"><path d="M3 1h3l1.5 4-2 1.2a9 9 0 0 0 4.3 4.3L11 8.5 15 10v3a2 2 0 0 1-2 2A12 12 0 0 1 1 3a2 2 0 0 1 2-2z"/></svg>212 555 0147</li>
        <li><svg viewBox="0 0 16 16" aria-hidden="true"><path d="M4 1h8v4H4zM1 6h14v6h-3v3H4v-3H1zM5 10v4h6v-4z"/></svg>212 555 0190</li>
        <li><svg viewBox="0 0 16 16" aria-hidden="true"><path d="M1 3h14v10H1zM2.5 4.5 8 9l5.5-4.5z"/></svg>info@quarry7.example</li>
      </ul>
      <p class="address">Address line goes here<br>Second line here pincode</p>
    </div>
    <p class="web">www.<span class="accent">quarry</span>.dev</p>
  </section>
</body>
</html>
```